Business cards and letterhead
cards and letterhead
Thanks all designers for your hard work.
Does anybody have anything different than just the swirl line through it?
I realy want the web address to stand out somehow, everybody just keep putting it in small letters...
Let's just leave off the email and make the web address stand out better.
creater I like #18 in black, the RT gets lost on the background. could it have a small white outline or something so it stands out. Website address must be on there, my email is not that important. Thanks
I like the color on there it makes it pop.
I want the web address to stand out. Thanks

```html
<!DOCTYPE html>
<html lang="en">
<head>
<meta charset="utf-8">
<title>RT Auto Sales – Stationery Set</title>
<link href="https://fonts.googleapis.com/css2?family=Archivo+Black&family=Roboto:wght@400;700&display=swap" rel="stylesheet">
<style>
  :root{
    --bg:#e6e6e6;
    --paper:#ffffff;
    --navy:#0d2a6e;
    --blue:#1f4fb4;
    --blue-light:#5d87d8;
    --red:#d0161c;
    --ink:#333b4a;
    --grey:#9aa1ad;
    --flap-dark:#1b1b1e;
  }
  *{box-sizing:border-box;margin:0;padding:0}
  html,body{width:1200px;height:533px;overflow:hidden;background:var(--bg);font-family:"Roboto",Arial,sans-serif}
  .canvas{position:relative;width:1200px;height:533px}
  .sheet{position:absolute;background:var(--paper);box-shadow:0 2px 6px rgba(0,0,0,.18);overflow:hidden}
  .band{position:absolute;left:0;bottom:0;width:100%}
  .logo{position:absolute;font-family:"Archivo Black",Arial,sans-serif;color:var(--navy);line-height:1;white-space:nowrap}
  .logo-dot{display:inline-block;background:var(--red);border-radius:50%;vertical-align:middle}
  .web{position:absolute;font-family:"Archivo Black",Arial,sans-serif;color:var(--red);white-space:nowrap;letter-spacing:.02em}
  .contact{position:absolute;color:#fff;font-size:7px;line-height:1.45}
  .contact strong{font-size:9px;display:block}

  /* business cards */
  .card{left:48px;width:204px;height:124px}
  .card-front{top:106px}
  .card-back{top:268px}
  .card .logo{left:14px;top:16px;font-size:21px}
  .card .logo .logo-dot{width:9px;height:9px;margin-left:4px}
  .card .web{left:14px;top:46px;font-size:13px}
  .card .contact{left:14px;bottom:10px}
  .card .contact-right{left:auto;right:12px;text-align:right}

  /* letterhead */
  .letterhead{left:290px;top:30px;width:288px;height:476px}
  .letterhead .logo{left:20px;top:30px;font-size:19px}
  .letterhead .logo .logo-dot{width:8px;height:8px;margin-left:4px}
  .letterhead .web{left:20px;top:54px;font-size:10px}
  .letterhead .address{position:absolute;right:14px;top:24px;width:76px;font-size:6px;color:var(--ink);line-height:1.6;border-left:2px solid var(--red);padding-left:6px}
  .vehicle-art{position:absolute;left:90px;top:300px;width:170px;height:90px;border-radius:30px 40px 12px 12px;background:radial-gradient(ellipse at 50% 60%,rgba(150,160,175,.22),rgba(150,160,175,0) 70%)}

  /* envelopes */
  .env-back{left:880px;top:70px;width:290px;height:150px}
  .env-open{left:860px;top:150px;width:300px;height:165px}
  .env-front{left:660px;top:318px;width:226px;height:180px}
  .env-front .logo{left:16px;top:26px;font-size:21px}
  .env-front .logo .logo-dot{width:9px;height:9px;margin-left:4px}
  .env-front .web{left:16px;top:54px;font-size:10px}
  .env-front .return{position:absolute;left:16px;top:72px;font-size:6px;color:var(--ink)}
  .flap-web{position:absolute;left:0;width:100%;text-align:center;font-family:"Archivo Black",Arial,sans-serif;font-size:10px;white-space:nowrap;line-height:1}
  .flap-logo{position:absolute;left:0;width:100%;text-align:center;font-family:"Archivo Black",Arial,sans-serif;font-size:10px;line-height:1}
</style>
</head>
<body>
<main class="canvas">

  <section class="sheet card card-front" aria-label="Business card front">
    <svg class="band" viewBox="0 0 204 60" height="60" preserveAspectRatio="none">
      <defs>
        <linearGradient id="blueBand" x1="0" y1="0" x2="1" y2="0">
          <stop offset="0" stop-color="#0d2a6e"/><stop offset=".55" stop-color="#1f4fb4"/><stop offset="1" stop-color="#5d87d8"/>
        </linearGradient>
      </defs>
      <path d="M0 14 C70 4 140 30 204 6 L204 60 L0 60Z" fill="url(#blueBand)"/>
      <path d="M0 10 C70 0 140 26 204 2" stroke="#d0161c" stroke-width="2.5" fill="none"/>
    </svg>
    <div class="logo">RT Auto Sales<span class="logo-dot"></span></div>
    <div class="web">WWW.RTMOTORLOT.BIZ</div>
    <div class="contact"><strong>Dana Morel</strong>Sales Manager</div>
    <div class="contact contact-right">(555) 014-2290<br>(555) 014-2291</div>
  </section>

  <section class="sheet card card-back" aria-label="Business card back">
    <svg class="band" viewBox="0 0 204 60" height="60" preserveAspectRatio="none">
      <path d="M0 14 C70 4 140 30 204 6 L204 60 L0 60Z" fill="url(#blueBand)"/>
      <path d="M0 10 C70 0 140 26 204 2" stroke="#d0161c" stroke-width="2.5" fill="none"/>
    </svg>
    <div class="logo">RT Auto Sales<span class="logo-dot"></span></div>
    <div class="web">WWW.RTMOTORLOT.BIZ</div>
    <div class="contact"><strong>Dana Morel</strong>Sales Manager</div>
    <div class="contact contact-right">Ph (555) 014-2290<br>2210 Harbor St, Velkaspire7</div>
  </section>

  <section class="sheet letterhead" aria-label="Letterhead">
    <div class="logo">RT Auto Sales<span class="logo-dot"></span></div>
    <div class="web">WWW.RTMOTORLOT.BIZ</div>
    <div class="address">2210 Harbor St<br>Velkaspire7, TX 75001<br>(555) 014-2290<br>(555) 014-2291</div>
    <div class="vehicle-art" role="img" aria-label="Faint pickup truck graphic"></div>
    <svg class="band" viewBox="0 0 288 70" height="70" preserveAspectRatio="none">
      <path d="M0 30 C100 10 190 50 288 16 L288 70 L0 70Z" fill="url(#blueBand)"/>
      <path d="M0 24 C100 4 190 44 288 10" stroke="#d0161c" stroke-width="3" fill="none"/>
    </svg>
  </section>

  <section class="sheet env-back" aria-label="Envelope back">
    <svg width="290" height="150" viewBox="0 0 290 150">
      <path d="M0 0 H290 V40 C220 95 70 95 0 40Z" fill="var(--flap-dark)"/>
      <path d="M0 40 C70 95 220 95 290 40" stroke="#d0161c" stroke-width="2" fill="none"/>
      <path d="M0 150 L120 90 M290 150 L170 90" stroke="#e2e4e8" stroke-width="1"/>
    </svg>
    <div class="flap-web" style="top:50px;color:#fff">WWW.RTMOTORLOT.BIZ</div>
  </section>

  <section class="sheet env-open" aria-label="Envelope with open flap">
    <svg width="300" height="165" viewBox="0 0 300 165">
      <path d="M0 0 C70 55 230 55 300 0 V30 C230 95 70 95 0 30Z" fill="url(#blueBand)"/>
      <path d="M0 30 C70 95 230 95 300 30" stroke="#d0161c" stroke-width="2.5" fill="none"/>
      <path d="M0 165 L130 100 M300 165 L170 100" stroke="#e2e4e8" stroke-width="1"/>
    </svg>
    <div class="flap-logo" style="top:46px;color:#fff">RT Auto Sales</div>
    <div class="flap-web" style="top:60px;color:#fff;font-size:9px">WWW.RTMOTORLOT.BIZ</div>
  </section>

  <section class="sheet env-front" aria-label="Envelope front">
    <div class="logo">RT Auto Sales<span class="logo-dot"></span></div>
    <div class="web">WWW.RTMOTORLOT.BIZ</div>
    <div class="return">2210 Harbor St, Velkaspire7 TX 75001</div>
    <svg class="band" viewBox="0 0 226 50" height="50" preserveAspectRatio="none">
      <path d="M0 20 C80 6 150 34 226 10 L226 50 L0 50Z" fill="url(#blueBand)"/>
      <path d="M0 15 C80 1 150 29 226 5" stroke="#d0161c" stroke-width="2.5" fill="none"/>
    </svg>
  </section>

</main>
</body>
</html>
```